Excel Template (Branded)

I have a number of reports that I create in Excel. I would like them to be branded instead of generic. Creating a template that I could use for all of my reports would be ideal. I would like to use the colours and logo of my website fernwidget.ca for branding ideas.

Target Market(s)

Everyday investors over the age of 18

Industry/Entity Type

investment

Requirements
Must have
• Professional design that will be shared with readers and subscribers of my blog
Nice to have
• clean professional design elements

```html
<!DOCTYPE html>
<html lang="en">
<head>
<meta charset="utf-8">
<title>10YR Compound Annual Growth Rates – Fern Widget</title>
<link href="https://fonts.googleapis.com/css2?family=Carlito:wght@400;700&family=Arimo:wght@700&display=swap" rel="stylesheet">
<style>
  :root{
    --navy-deep:#1d3a66;
    --navy-light:#3467a6;
    --navy-tab:#0f2444;
    --green-top:#0f9152;
    --green-bottom:#0a7b16;
    --head-year:#4f81bd;
    --head-price:#2f5597;
    --head-yield:#1f3864;
    --row-dark:#b8cce4;
    --row-light:#dce6f1;
    --brand-green:#0b8a48;
    --white:#ffffff;
  }
  *{margin:0;padding:0;box-sizing:border-box}
  html,body{width:1200px;height:692px;overflow:hidden;background:var(--white)}
  .canvas{position:relative;width:1200px;height:692px;overflow:hidden;font-family:"Carlito",Calibri,sans-serif;color:var(--white)}

  .brand{position:absolute;left:8px;top:30px;display:flex;align-items:center;gap:8px}
  .brand-dot{width:40px;height:40px;border-radius:50%;background:var(--navy-deep)}
  .brand-name{font-weight:700;font-size:30px;color:var(--brand-green);line-height:1}

  .title-bar{position:absolute;left:216px;top:1px;width:969px;height:49px;border-radius:0 10px 10px 0;
    background:linear-gradient(90deg,var(--navy-deep),var(--navy-light));border:2px solid #6e95cf;border-top:none;
    display:flex;align-items:center;justify-content:center;font-weight:700;font-size:25.8px;letter-spacing:.2px}

  .green{background:linear-gradient(180deg,var(--green-top) 0%,var(--green-top) 40%,var(--green-bottom) 100%)}

  .section-band{position:absolute;left:215px;top:58px;width:985px;height:44px}
  .section-band svg.dividers{position:absolute;left:0;top:0}
  .section{position:absolute;top:0;height:44px;display:flex;align-items:center;justify-content:center;gap:10px;
    font-weight:700;font-size:19.4px;letter-spacing:.3px}
  .section svg{flex:none}
  .s-div{left:0;width:545px;padding-left:50px}
  .s-price{left:547px;width:107px}
  .s-yield{left:657px;width:163px}
  .s-total{left:821px;width:164px}

  .cagr-tab{position:absolute;top:107px;height:16px;width:54px;background:var(--navy-tab);
    font-weight:700;font-size:12px;display:flex;align-items:center;justify-content:center;
    clip-path:polygon(0 0,88% 0,100% 35%,100% 100%,0 100%)}

  .table-head{position:absolute;left:1px;top:127px;width:1199px;height:21px;display:grid;
    grid-template-columns:54px 154px repeat(18,54px);column-gap:1px;
    font-family:"Arimo",Arial,sans-serif;font-weight:700;font-size:9.5px}
  .table-head span{display:flex;align-items:center;justify-content:center;white-space:nowrap}
  .h-year{background:var(--head-year)}
  .h-company{background:var(--head-year);justify-content:flex-start!important;padding-left:3px;font-size:12.5px}
  .h-price{background:var(--head-price)}
  .h-yield{background:var(--head-yield)}
  .h-cagr{background:var(--navy-tab)}

  .table-body{position:absolute;left:1px;top:149px;width:1199px;height:396px;
    background:
      linear-gradient(90deg,transparent 54px,var(--white) 54px 55px,transparent 55px 209px,var(--white) 209px 210px,transparent 210px),
      repeating-linear-gradient(180deg,var(--row-dark) 0 17px,var(--white) 17px 18px,var(--row-light) 18px 35px,var(--white) 35px 36px)}
  .table-cols{position:absolute;left:211px;top:149px;width:989px;height:396px;
    background:repeating-linear-gradient(90deg,transparent 0 54px,var(--white) 54px 55px)}

  .averages{position:absolute;top:554px;height:28px}
  .avg-label{left:211px;width:658px;display:flex;align-items:center;justify-content:center;font-weight:700;font-size:21px;
    clip-path:polygon(0 0,98.6% 0,100% 30%,100% 100%,0 100%)}
  .avg-cells{left:871px;width:329px;display:grid;grid-template-columns:repeat(6,54px);column-gap:1px;background:var(--white)}
  .avg-cells span{display:block}

  .note{position:absolute;left:214px;top:604px;width:986px;height:88px;padding:5px 6px;
    font-weight:700;font-size:15.2px;line-height:19px}
</style>
</head>
<body>
<div class="canvas">

  <div class="brand">
    <span class="brand-dot"></span>
    <span class="brand-name">Fern Widget</span>
  </div>

  <header class="title-bar">10YR-Compound Annual Growth Rates (CAGR) as of 01-01-2021</header>

  <div class="section-band green">
    <svg class="dividers" width="985" height="44" viewBox="0 0 985 44" aria-hidden="true">
      <g stroke="#ffffff" stroke-width="2" fill="none">
        <polyline points="533,0 546,12 546,44"/>
        <polyline points="643,0 656,12 656,44"/>
        <polyline points="808,0 821,12 821,44"/>
        <polyline points="973,0 985,10"/>
      </g>
    </svg>
    <div class="section s-div">Ten Years of Dividend Growth (Year-by-Year)
      <svg width="26" height="36" viewBox="0 0 26 36" aria-hidden="true">
        <text x="13" y="15" text-anchor="middle" font-family="Carlito,sans-serif" font-weight="700" font-size="17" fill="#fff">$</text>
        <path d="M13 17v13M13 24c-4-1-7-4-8-7 4 0 7 2 8 5M13 22c4-1 7-4 8-7-4 0-7 2-8 5" stroke="#fff" stroke-width="2" fill="#fff"/>
        <ellipse cx="13" cy="32" rx="8" ry="3" fill="#fff"/>
      </svg>
    </div>
    <div class="section s-price">Price
      <svg width="32" height="32" viewBox="0 0 32 32" aria-hidden="true">
        <circle cx="16" cy="16" r="14" stroke="#fff" stroke-width="2" fill="none"/>
        <circle cx="16" cy="16" r="10" stroke="#fff" stroke-width="1.5" fill="none"/>
        <text x="16" y="21" text-anchor="middle" font-family="Carlito,sans-serif" font-weight="700" font-size="14" fill="#fff">$</text>
      </svg>
    </div>
    <div class="section s-yield">Yield
      <svg width="32" height="32" viewBox="0 0 32 32" aria-hidden="true">
        <circle cx="16" cy="16" r="14" stroke="#fff" stroke-width="2" fill="none"/>
        <path d="M10 23v-4M14 23v-6M18 23v-8M22 23v-10M10 15l9-6M16 9h3v3" stroke="#fff" stroke-width="2" fill="none"/>
      </svg>
    </div>
    <div class="section s-total">Total return
      <svg width="30" height="28" viewBox="0 0 30 28" aria-hidden="true">
        <path d="M8 9a11 11 0 1 1 1 13" stroke="#fff" stroke-width="2.2" fill="none"/>
        <path d="M3 9h8l-4 5z" fill="#fff"/>
      </svg>
    </div>
  </div>

  <div class="cagr-tab" style="left:1036px">CAGR</div>
  <div class="cagr-tab" style="left:1091px">CAGR</div>
  <div class="cagr-tab" style="left:1146px">CAGR</div>

  <div class="table-head">
    <span class="h-year">Symbol</span>
    <span class="h-company">Company</span>
    <span class="h-year">2011</span><span class="h-year">2012</span><span class="h-year">2013</span><span class="h-year">2014</span><span class="h-year">2015</span>
    <span class="h-year">2016</span><span class="h-year">2017</span><span class="h-year">2018</span><span class="h-year">2019</span><span class="h-year">2020</span>
    <span class="h-price">$'11</span><span class="h-price">$'21</span>
    <span class="h-yield">YLD'11</span><span class="h-yield">YLD'21</span><span class="h-yield">10YOC</span>
    <span class="h-cagr">10Y TR</span><span class="h-cagr">10Y DG</span><span class="h-cagr">10Y PG</span>
  </div>

  <div class="table-body"></div>
  <div class="table-cols"></div>

  <div class="averages avg-label green">Averages</div>
  <div class="averages avg-cells">
    <span class="green"></span><span class="green"></span><span class="green"></span>
    <span class="green"></span><span class="green"></span><span class="green"></span>
  </div>

  <p class="note green">As successful dividend growth investors we understand that rising dividends are a foundation for higher share prices.<br>
  Here is the Compound Annual Growth Rate (CAGR) of dividends and CAGR of price over the last decade so that you can study the evidence that as the dividend grows, so does the price</p>

</div>
</body>
</html>
```